Vielen Dank für das tolle Ergebnis! Die Zusammenarbeit hat sehr gut geklappt, alle unsere Vorstellungen und Änderungswünsche wurden schnell umgesetzt, die Kommunikation verlief sehr angenehm und freundlich. Wir sind sehr zufrieden.
Zielgruppe
Wir sind ein junges Musikensemble für Alte Musik und veranstalten im Sommer unter dem Titel 'Talwiesener Abendklänge' ein kleines Festival in Talwiesen und Veßra (Thüringen). Neben zwei Open-Air Konzerten gibt es ein kostenloses Mit-Mach-Konzert für Kinder und einen musikalischen Gottesdiest mit Werke der Brennerzeit. Das Plakat soll in der Region Südthüringen aber auch im weiteren Umland aufgehängt werden und soll sich nicht nur an das klassische Konzertpublikum wenden sondern auch 'klassikfernes' Publikum für die Konzerte interessieren. Der Unterhaltungswert, das besondere Ambiente der Open-Air-Spielorte und die sommerliche, lockere Atmosphäre sollen im Vordergrund stehen. Wir möchten auch jüngeres Publikum mit dem Plakat ansprechen.
Aufgabenstellung
Das Design sollte nicht zu konservtiv sein. Wir möchten uns als aufgeschlossenenes, junges Ensemble präsentieren. "Alte Musik" soll nicht mit antiquiert und verstaubt assoziiert werden sondern mit innovativ, frisch und aktuell.
Die beiden Hauptkonzerte sind Open-Air, gespielt werden die "Giochi Armonici" von Tommaso Cavarelli, Musik zur Unterhaltung am Hof des Herzogs Pellucci in Mantua - italienische Renaissancemusik. Diese Musik hat einen stark unterhaltenden Charakter, ist sehr verspielt und leicht zugänglich. Es ist ein weltliches Programm mit sehr zweideutigen Texten. Gleichzeitig stehen die Konzerte im Kontext des Reformationsjubiläums 2017. Stichpunkte wäre für uns: Italien, Sommer, Barockmusik, Cavarelli, Unterhaltung, Open-Air, Burg Hohenwalde, Renaissance, Reformation,...
Gerne sollte ein Foto des Ensembles und unser Logo integriert werden.
Das Brenner-Logo muss drauf sein (oben rechts).
Auf dem Plakat sollen folgende Informationen stehen
Obertitel "Talwiesener Abendklänge 2017"
Untertitel "Renaissancemusik zum Reformationsjahr"
Konzerttermine
VVK-Stellen
Preise
evtl. website und kontakt
Unten benötigen wir eine Logoleiste für Sponsoren.
Format ist DIN A2.
Mehr Infos zum Programm und dem Ensemble im Anhang.

```html
<!DOCTYPE html>
<html lang="de">
<head>
<meta charset="utf-8">
<title>Talwiesener Abendklänge 2017 – Plakat</title>
<link rel="stylesheet" href="https://fonts.googleapis.com/css2?family=EB+Garamond:wght@400;500;600;700&display=swap">
<style>
  :root {
    --sky: #1a9fdc;
    --amber: #f39a17;
    --white: #ffffff;
    --backdrop: #ecebe7;
    --font-main: "EB Garamond", Georgia, serif;
  }
  * { box-sizing: border-box; margin: 0; padding: 0; }
  html, body { width: 1200px; height: 900px; overflow: hidden; }
  body { background: var(--backdrop); font-family: var(--font-main); position: relative; }

  .poster {
    position: absolute; left: 305px; top: 33px; width: 590px; height: 834px;
    display: grid; grid-template-columns: 1fr 1fr; grid-template-rows: 1fr 1fr;
    box-shadow: 0 6px 18px rgba(0,0,0,.18);
  }
  .event { position: relative; color: var(--white); overflow: hidden; }
  .event--sky { background: var(--sky); }
  .event--amber { background: var(--amber); }

  .date, .info, .venue-block { z-index: 3; }

  .date { position: absolute; left: 38px; right: 30px; }
  .date__day { font-size: 74px; line-height: 1; display: block; font-weight: 400; }
  .date__row { display: flex; justify-content: space-between; align-items: baseline; margin-top: -6px; }
  .date__month { font-size: 38px; letter-spacing: 1px; }
  .date__time { font-size: 34px; }
  .accent-amber { color: var(--amber); }
  .accent-sky { color: var(--sky); }

  .date--top { top: 30px; }
  .date--bottom { top: 268px; }

  .info { position: absolute; }
  .info--start { left: 38px; text-align: left; }
  .info--end { right: 42px; text-align: right; }
  .info__title { font-size: 29px; font-weight: 600; line-height: 1.05; }
  .info__title--caps { font-size: 27px; letter-spacing: .5px; text-transform: uppercase; }
  .info__subtitle { font-size: 12.5px; letter-spacing: .4px; text-transform: uppercase; margin-top: 2px; line-height: 1.25; font-weight: 500; }
  .info__detail { font-size: 10px; letter-spacing: .3px; text-transform: uppercase; margin-top: 16px; line-height: 1.45; }
  .info__detail--tight { margin-top: 12px; }
  .venue { font-size: 13.5px; font-weight: 700; text-transform: uppercase; letter-spacing: .3px; }
  .venue__sub { font-size: 9px; text-transform: uppercase; letter-spacing: .3px; display: block; margin-top: 2px; }
  .venue-block { position: absolute; }

  .partner-name {
    position: absolute; top: 96px; right: 42px;
    color: var(--white); font-size: 14px; font-weight: 600; letter-spacing: .5px; text-transform: uppercase;
    z-index: 3;
  }

  .ensemble-name {
    position: absolute; left: 402px; top: 462px; z-index: 3;
    color: var(--white); font-size: 26px; font-weight: 500;
  }

  .venue-photo {
    position: absolute; left: 140px; top: 285px; width: 290px; height: 270px; z-index: 1;
    background: linear-gradient(180deg, rgba(110,140,175,.8) 0%, rgba(170,150,120,.9) 45%, rgba(150,135,115,.85) 65%, rgba(110,140,175,.6) 100%);
    -webkit-mask-image: radial-gradient(ellipse 50% 50% at 55% 50%, #000 55%, transparent 100%);
            mask-image: radial-gradient(ellipse 50% 50% at 55% 50%, #000 55%, transparent 100%);
  }
</style>
</head>
<body>
  <main class="poster" aria-label="Talwiesener Abendklänge 2017">

    <section class="event event--sky">
      <div class="date date--top">
        <span class="date__day accent-amber">30.</span>
        <div class="date__row"><span class="date__month">JUNI</span><span class="date__time">19:30</span></div>
      </div>
      <div class="info info--start" style="top:180px">
        <h2 class="info__title">Giochi Armonici</h2>
        <p class="info__subtitle">Italienische Sommernacht</p>
        <p class="info__detail">Tommaso Cavarelli,<br>Madrigali Amorosi</p>
      </div>
      <div class="venue-block info--start" style="top:288px">
        <p class="venue accent-amber">Kloster Auenried,<span class="venue__sub">Ruine der Klosterkirche</span></p>
      </div>
    </section>

    <section class="event event--amber">
      <span class="partner-name">Brenner</span>
      <div class="date date--top">
        <span class="date__day accent-sky">01.</span>
        <div class="date__row"><span class="date__month">JULI</span><span class="date__time">11:00</span></div>
      </div>
      <div class="info info--end" style="top:180px">
        <h2 class="info__title info__title--caps">Barockstar</h2>
        <p class="info__subtitle">Cavarelli am Hof der<br>Herzöge Pellucci in Mantua</p>
        <p class="info__detail info__detail--tight">Kinder Mit-Mach-Konzert<br>für alle ab 4 Jahren</p>
      </div>
      <div class="venue-block info--end" style="top:288px">
        <p class="venue accent-sky">Kloster Auenried,<span class="venue__sub">Ruine der Klosterkirche</span></p>
      </div>
    </section>

    <section class="event event--amber">
      <div class="info info--start" style="top:108px">
        <h2 class="info__title">Giochi Armonici</h2>
        <p class="info__subtitle">Italienische Sommernacht</p>
        <p class="info__detail">Tommaso Cavarelli,<br>Madrigali Amorosi</p>
      </div>
      <div class="venue-block info--start" style="top:228px">
        <p class="venue accent-sky">Hohenwalder Burghof</p>
      </div>
      <div class="date date--bottom">
        <span class="date__day">01.</span>
        <div class="date__row"><span class="date__month">JULI</span><span class="date__time">19:30</span></div>
      </div>
    </section>

    <section class="event event--sky">
      <div class="info info--end" style="top:90px">
        <h2 class="info__title info__title--caps" style="font-size:30px">Ein<br>Feste Burg</h2>
        <p class="info__detail info__detail--tight">Musikalische Gestaltung des Gottes-<br>dienstes durch Mitglieder des<br>Ensembles Serica</p>
      </div>
      <div class="venue-block info--end" style="top:228px">
        <p class="venue accent-amber">Marienkirche,<span class="venue__sub">Talwiesen</span></p>
      </div>
      <div class="date date--bottom">
        <span class="date__day accent-amber">02.</span>
        <div class="date__row"><span class="date__month">JULI</span><span class="date__time">19:30</span></div>
      </div>
    </section>

    <div class="venue-photo" role="img" aria-label="Fotocollage der Spielorte: Klosterkirche, Fachwerkhaus und Burgfassade, gespiegelt"></div>

    <span class="ensemble-name">Serica</span>
  </main>
</body>
</html>
```